CBD Banner Ad for Print and Zentrix

I we would like a modern European chic that we can use in a 1/4 page ad in our local magazine and also use as our banner ad in the Zentrix ad searches. <br/><br/>We are a high end CBD boutique shop that has their own brand as well as a carefully curated selection of the top end CBD products out on the market. The final design should promote the health and well being that we are trying to live ourselves. We DO NOT want the use of marijuana paraphernalia or like substances. Think Yoga Studio meets Morvik inside of a health store. <br/><br/>Use any images you would like...I have attached a sample product render as well as the inside of our store...but take this in the direction you would like.<br/><br/>The winner will have the added bonus of being able to create 10 more ads for us in the next 6 months.

Target Market(s)

Our target market are the middle to upperclass professional workers that want to take CBD but were afraid due to misinformation or stigma

Font styles to use
Sans Serif

Colors
33b8a4
86cfc6
0792cd
3277b5
85acd3

Requirements
Must have
• A good clean modern design.
• Natural. Organic. Crisp. Welcoming.
Nice to have
• Opal Meadow
• CBD for wellness. CBD for life.
• The font we use for the rest of our campaigns is Adam.
Should not have
• Absolutely NO marijuana leaves, paraphernalia, or references. We are working hard to educate people and get rid of the stigma.

```html
<!DOCTYPE html>
<html lang="en">
<head>
<meta charset="utf-8">
<title>Opal Meadow – CBD Ad Set</title>
<link href="https://fonts.googleapis.com/css2?family=Josefin+Sans:wght@100;200;300&family=Mulish:wght@400&display=swap" rel="stylesheet">
<style>
  :root {
    --page-bg: #dfdfdf;
    --label: #3a3a3a;
    --white: #ffffff;
    --sage: #86a664;
    --gold: #b89b5e;
    --product-light: #f2f3f5;
    --product-lilac: #c9c6e6;
    --product-cream: #efe6d2;
  }
  * { margin: 0; padding: 0; box-sizing: border-box; }
  html, body { width: 1200px; height: 1087px; overflow: hidden; }
  body { background: var(--page-bg); position: relative; font-family: "Josefin Sans", sans-serif; }

  .section-title {
    position: absolute; top: 148px;
    font-family: "Mulish", sans-serif; font-weight: 400;
    font-size: 24px; color: var(--label); letter-spacing: 0.5px;
  }
  .size-label {
    position: absolute;
    font-family: "Mulish", sans-serif; font-size: 17px; color: var(--label);
  }
  .ad { position: absolute; background: var(--white); overflow: hidden; }
  .brand-name {
    position: absolute; color: var(--gold); font-weight: 200;
    white-space: nowrap; text-align: center; letter-spacing: 1px;
  }
  .product-render { position: absolute; z-index: 2; border-radius: 6px;
    background: linear-gradient(180deg, var(--product-light) 0%, var(--product-light) 45%, var(--product-lilac) 80%, var(--product-cream) 100%); }
  .green-band { position: absolute; z-index: 1; left: 0; right: 0; background: var(--sage); }
  .band-text { position: absolute; z-index: 3; color: var(--white); white-space: nowrap; }
  .cta {
    position: absolute; z-index: 3; background: var(--white); color: var(--gold);
    font-family: "Mulish", sans-serif; display: flex; align-items: center; justify-content: center;
    white-space: nowrap;
  }

  /* Print ad */
  .print-ad { left: 139px; top: 205px; width: 420px; height: 700px; }
  .print-ad .brand-name { left: 0; width: 420px; top: 52px; font-size: 40px; }
  .print-ad .product-render { left: 70px; top: 155px; width: 280px; height: 232px; }
  .print-ad .green-band { top: 361px; bottom: 0; }
  .print-headline { left: 0; width: 420px; top: 419px; text-align: center;
    font-weight: 100; font-size: 66px; letter-spacing: 2px; line-height: 1; }
  .print-rule { position: absolute; z-index: 3; left: 163px; top: 505px; width: 94px; height: 1px; background: var(--white); }
  .print-tagline { left: 0; width: 420px; top: 524px; text-align: center;
    font-weight: 100; font-size: 37px; letter-spacing: 3px; line-height: 33px; }
  .print-url { left: 0; width: 420px; top: 640px; text-align: center;
    font-weight: 200; font-size: 19px; letter-spacing: 0.5px; }

  /* Rectangle banner */
  .rect-ad { left: 631px; top: 205px; width: 202px; height: 168px; }
  .rect-ad .brand-name { left: 8px; width: 100px; top: 32px; font-size: 15px; }
  .rect-ad .product-render { left: 114px; top: 12px; width: 76px; height: 80px; }
  .rect-ad .green-band { top: 82px; bottom: 0; }
  .rect-tagline { left: 0; width: 202px; top: 97px; text-align: center;
    font-weight: 200; font-size: 15px; letter-spacing: 0.8px; line-height: 14px; }
  .rect-ad .cta { left: 55px; top: 133px; width: 92px; height: 22px; font-size: 9px; }

  /* Leaderboard banner */
  .wide-ad { left: 631px; top: 439px; width: 437px; height: 54px; }
  .wide-ad .brand-name { left: 6px; width: 82px; top: 20px; font-size: 12px; }
  .wide-ad .product-render { left: 92px; top: 5px; width: 116px; height: 45px; }
  .wide-ad .green-band { left: 219px; top: 0; bottom: 0; right: 0; }
  .wide-tagline { left: 231px; width: 116px; top: 18px;
    font-weight: 200; font-size: 10px; letter-spacing: 0.2px; line-height: 10px; }
  .wide-ad .cta { left: 353px; top: 16px; width: 65px; height: 23px; font-size: 8px; }
</style>
</head>
<body>
  <h2 class="section-title" style="left:138px">LOCAL AD</h2>
  <h2 class="section-title" style="left:629px">ZENTRIX AD</h2>

  <section class="ad print-ad">
    <div class="brand-name">Opal Meadow</div>
    <div class="product-render" role="img" aria-label="Product render of three CBD jars: gummies, melatonin softgels and curcumin softgels"></div>
    <div class="green-band"></div>
    <div class="band-text print-headline">CBD</div>
    <div class="print-rule"></div>
    <div class="band-text print-tagline">FOR WELLNESS<br>AND LIFE</div>
    <div class="band-text print-url">WWW.OPALMEADOW.COM</div>
  </section>
  <div class="size-label" style="left:138px; top:915px">15X25CM</div>

  <section class="ad rect-ad">
    <div class="brand-name">Opal Meadow</div>
    <div class="product-render" role="img" aria-label="Product render of two CBD jars"></div>
    <div class="green-band"></div>
    <div class="band-text rect-tagline">CBD FOR WELLNESS<br>AND LIFE</div>
    <div class="cta">CHECK NOW</div>
  </section>
  <div class="size-label" style="left:629px; top:383px">336X280PX</div>

  <section class="ad wide-ad">
    <div class="brand-name">Opal Meadow</div>
    <div class="product-render" role="img" aria-label="Product render of a row of CBD jars"></div>
    <div class="green-band"></div>
    <div class="band-text wide-tagline">HIGH-END CBD FOR<br>WELLNESS AND LIFE</div>
    <div class="cta">CHECK NOW</div>
  </section>
  <div class="size-label" style="left:629px; top:504px">728X90PX</div>
</body>
</html>
```